SkyVarro logo and website for a cloud solution provider in the UK market

Produce a logo with strong brand identity and a website themed similar to the log design.

The website is for a company called SkyVarro limited. SkyVarro specialises in migrating businesses from their on premise infrastructure to cloud services such as Deskwell365, Torvane and also Pelligrin Host Systems.

We offer migration and management services to allow customers to focus on their core business letting SkyVarro manage their business IT services and infratructure.

The design should leverage the Quillent partner information for the cost savings of migrating on premise solutions to the cloud. The website should also leverage Quillents content syndication to help with marketing materials and campaigns. the website links can be found here: https://setandrun.quillent-example.com

The website must be suitable for both desktop and mobile platforms including smartphones and tablets.

The design should communicate financial savings, confidence and user flexibility.

Reason: I need a website which will easy render on mobile devices which isn't too cluttered and has clear areas where I can insert Quillent syndicate banner content of sizes 180x150, 600x90 or 600x250. For details of Quillent syndicated content please see: http://setandrun.quillent-example.com

Target Market(s)

Small to medium companies who use on premise email, Filemesh, and web infrastructure who want to migrate their business safely to the cloud.

Industry/Entity Type

It Company

Logo Text

SkyVarro

Number of Pages Required

4 page

```html
<!DOCTYPE html>
<html lang="en">
<head>
<meta charset="utf-8">
<title>SkyVarro limited — Cloud Migration Services</title>
<link rel="stylesheet" href="https://fonts.googleapis.com/css2?family=Open+Sans:wght@400;600;700&display=swap">
<style>
:root{
  --blue:#2a8bd0;
  --blue-dark:#1c6aa8;
  --blue-deep:#1a4f7d;
  --navy:#1d3f63;
  --navy-dark:#163250;
  --accent:#2fa5e6;
  --ink:#333a41;
  --muted:#7b848c;
  --line:#e3e7ea;
  --soft:#f3f5f7;
  --white:#ffffff;
}
*{box-sizing:border-box;margin:0;padding:0}
html,body{width:1200px;height:2188px;overflow:hidden}
body{font-family:"Open Sans",Arial,sans-serif;color:var(--ink);background:var(--white);position:relative}
.header{height:72px;display:flex;align-items:center;justify-content:space-between;padding:0 40px 0 44px;background:var(--white)}
.brand{display:flex;align-items:center;gap:10px;font-weight:700;font-size:22px;color:var(--blue-dark)}
.brand-mark{width:18px;height:18px;border-radius:50%;background:var(--blue)}
.nav{display:flex;gap:0}
.nav a{font-size:12px;font-weight:600;color:var(--ink);text-decoration:none;padding:0 24px;height:72px;display:flex;align-items:center;letter-spacing:.4px}
.nav a.active{color:var(--blue)}
.hero{position:relative;height:430px;background:linear-gradient(180deg,#3196d8 0%,#2279bd 100%);color:var(--white);overflow:hidden}
.hero-text{position:absolute;left:100px;top:80px;width:420px}
.hero-text h1{font-size:58px;font-weight:700;line-height:1}
.hero-text h2{font-size:19px;font-weight:600;margin:14px 0 16px}
.hero-text p{font-size:13px;line-height:20px;opacity:.9}
.btn{display:inline-block;margin-top:22px;background:var(--accent);color:var(--white);font-size:11px;font-weight:700;padding:11px 26px;border-radius:20px;letter-spacing:.4px;border:1px solid rgba(255,255,255,.4)}
.hero-art{position:absolute;left:590px;top:30px;width:520px;height:380px;border-radius:8px;background:radial-gradient(ellipse at 50% 35%,rgba(255,255,255,.35),rgba(255,255,255,.08) 70%)}
.arrow{position:absolute;top:195px}
.arrow.left{left:18px}.arrow.right{right:18px}
.welcome{text-align:center;padding:60px 150px 0}
.welcome h3{font-size:32px;font-weight:400;color:var(--ink)}
.welcome h3 span{color:var(--blue)}
.welcome p{font-size:11px;line-height:18px;color:var(--muted);margin-top:20px}
.services{display:flex;margin:36px 90px 0;height:150px;background:var(--blue)}
.service{flex:1;text-align:center;color:var(--white);padding:22px 36px;border-right:1px solid rgba(255,255,255,.3)}
.service:last-child{border-right:0}
.service h4{font-size:13px;font-weight:700;margin:10px 0 8px;letter-spacing:.3px}
.service p{font-size:10.5px;line-height:16px;opacity:.9}
.specialise{margin-top:40px;height:530px;background:var(--soft);position:relative;border-top:1px solid var(--line)}
.specialise-text{position:absolute;left:100px;top:40px;width:500px}
.specialise-text h3{font-size:20px;font-weight:600;line-height:27px;color:var(--ink)}
.specialise-text p{font-size:11px;line-height:17px;color:var(--muted);margin-top:14px}
.checks{list-style:none;margin-top:22px}
.checks li{display:flex;align-items:center;gap:12px;font-size:12px;color:var(--ink);margin-bottom:18px}
.specialise-art{position:absolute;left:650px;top:40px;width:470px;height:430px;border-radius:8px;background:radial-gradient(ellipse at 50% 50%,#bfe3f7,#e9f4fb 70%)}
.lower{display:flex;padding:40px 100px 0;gap:40px}
.col-title{font-size:14px;font-weight:700;letter-spacing:.4px;color:var(--ink);padding-bottom:12px;border-bottom:1px solid var(--line);margin-bottom:20px}
.news{flex:1}
.news-item{display:flex;gap:18px;margin-bottom:22px}
.news-thumb{width:140px;height:90px;flex:none;background:linear-gradient(180deg,#6fb8ea,#2f86c6)}
.news-item h5{font-size:13px;font-weight:600}
.news-date{font-size:12px;font-weight:700;color:var(--blue);margin:4px 0 6px}
.news-item p{font-size:10.5px;line-height:16px;color:var(--muted)}
.testimonials{flex:1}
.quote{border:1px solid var(--line);padding:20px 24px;font-size:11px;line-height:18px;color:var(--muted);background:var(--white)}
.quote-nav{text-align:right;margin-top:-8px}
.person{display:flex;align-items:center;gap:16px;margin-top:20px}
.avatar{width:64px;height:64px;border-radius:50%;background:#c9d6df}
.person b{color:var(--blue);font-size:12px;font-weight:600}
.person span{font-size:12px;color:var(--muted)}
.footer{position:absolute;left:0;right:0;top:1876px;height:276px;background:var(--navy);color:#c8d6e3;display:flex;padding:40px 100px 0;gap:40px}
.footer > div{flex:1}
.footer h6{font-size:13px;font-weight:700;color:var(--white);margin-bottom:16px;letter-spacing:.4px}
.footer p,.footer li{font-size:10.5px;line-height:17px}
.footer ul{list-style:none}
.footer li::before{content:"› ";color:var(--accent)}
.subscribe{display:flex;margin-top:14px}
.subscribe span{flex:1;background:var(--white);color:var(--muted);font-size:10px;padding:9px 10px}
.subscribe b{background:var(--blue-deep);color:var(--white);font-size:10px;padding:9px 12px;border:1px solid #3b6c9a}
.contact-line{display:flex;gap:8px;align-items:center;margin-top:6px}
.bottom{position:absolute;left:0;right:0;top:2152px;height:36px;background:var(--navy-dark);color:#9fb3c6;font-size:10px;display:flex;align-items:center;justify-content:center}
</style>
</head>
<body>
<header class="header">
  <div class="brand"><span class="brand-mark"></span>SkyVarro</div>
  <nav class="nav">
    <a class="active">HOME</a><a>ABOUT US</a><a>SERVICES</a><a>NEWS</a><a>CONTACT US</a>
  </nav>
</header>

<section class="hero">
  <div class="hero-text">
    <h1>SkyVarro</h1>
    <h2>SkyVarro specializes in migrating businesses</h2>
    <p>We move your email, files and web services to the cloud with care, so your team keeps working while we handle the change.</p>
    <span class="btn">MORE INFORMATION</span>
  </div>
  <div class="hero-art" role="img" aria-label="Cloud services illustration linking a laptop, tablet, phone and desktop"></div>
  <svg class="arrow left" width="14" height="24" viewBox="0 0 14 24"><path d="M12 2 2 12l10 10" fill="none" stroke="#fff" stroke-width="2.5"/></svg>
  <svg class="arrow right" width="14" height="24" viewBox="0 0 14 24"><path d="M2 2l10 10L2 22" fill="none" stroke="#fff" stroke-width="2.5"/></svg>
</section>

<section class="welcome">
  <h3>Welcome To <span>SkyVarro limited</span></h3>
  <p>SkyVarro helps small and medium companies leave ageing on premise servers behind. We plan each move, test every mailbox and file share, and keep downtime close to zero. Our engineers manage your cloud estate day to day, watch costs, apply updates and answer questions in plain English. You pay a clear monthly fee, gain room to grow, and spend your time on the work that matters to your customers rather than on hardware, licences and late night fixes in the server room.</p>
</section>

<section class="services">
  <div class="service">
    <svg width="26" height="26" viewBox="0 0 26 26"><rect x="3" y="3" width="20" height="20" fill="none" stroke="#fff" stroke-width="2"/><path d="M8 9h10M8 13h10M8 17h6" stroke="#fff" stroke-width="2"/></svg>
    <h4>DESKWELL365</h4>
    <p>Email, calendars and office apps hosted for you, always current and reachable from any device your staff use.</p>
  </div>
  <div class="service">
    <svg width="26" height="26" viewBox="0 0 26 26"><rect x="3" y="3" width="20" height="6" rx="1" fill="none" stroke="#fff" stroke-width="2"/><rect x="3" y="10" width="20" height="6" rx="1" fill="none" stroke="#fff" stroke-width="2"/><rect x="3" y="17" width="20" height="6" rx="1" fill="none" stroke="#fff" stroke-width="2"/><circle cx="7" cy="6" r="1.2" fill="#fff"/><circle cx="7" cy="13" r="1.2" fill="#fff"/><circle cx="7" cy="20" r="1.2" fill="#fff"/></svg>
    <h4>QUILLENT TORVANE</h4>
    <p>Servers, storage and backups that scale with demand, so you only pay for the capacity you really need.</p>
  </div>
  <div class="service">
    <svg width="26" height="26" viewBox="0 0 26 26"><rect x="3" y="4" width="20" height="14" fill="none" stroke="#fff" stroke-width="2"/><path d="M9 22h8M13 18v4" stroke="#fff" stroke-width="2"/></svg>
    <h4>PELLIGRIN HOST SYSTEMS</h4>
    <p>Reliable web hosting and compute for sites and apps, set up, secured and looked after by our team.</p>
  </div>
</section>

<section class="specialise">
  <div class="specialise-text">
    <h3>SkyVarro specialises in migrating businesses<br>from their on premise infrastructure to cloud services</h3>
    <p>We review what you run today, map a safe path to the cloud and move it in stages. After launch we stay on as your IT partner, keeping systems healthy, secure and good value month after month for your business.</p>
    <ul class="checks">
      <li><svg width="16" height="16" viewBox="0 0 16 16"><path d="M2 8l4 4 8-8" fill="none" stroke="#2a8bd0" stroke-width="2.5"/></svg>We deliver Top Technology</li>
      <li><svg width="16" height="16" viewBox="0 0 16 16"><path d="M2 8l4 4 8-8" fill="none" stroke="#2a8bd0" stroke-width="2.5"/></svg>High customer retention rate</li>
      <li><svg width="16" height="16" viewBox="0 0 16 16"><path d="M2 8l4 4 8-8" fill="none" stroke="#2a8bd0" stroke-width="2.5"/></svg>We always return e-mails and calls within one business day</li>
      <li><svg width="16" height="16" viewBox="0 0 16 16"><path d="M2 8l4 4 8-8" fill="none" stroke="#2a8bd0" stroke-width="2.5"/></svg>Affordable pricing offers</li>
    </ul>
  </div>
  <div class="specialise-art" role="img" aria-label="Cloud services illustration surrounded by connected app icons"></div>
</section>

<section class="lower">
  <div class="news">
    <div class="col-title">OUR NEWS</div>
    <div class="news-item">
      <div class="news-thumb" role="img" aria-label="Photo of a bright sky with clouds"></div>
      <div>
        <h5>Sed ut perspiciatis unde omnis</h5>
        <div class="news-date">18 - MARCH 2015</div>
        <p>Our latest guide explains how growing firms cut running costs by moving mail and files to the cloud.</p>
      </div>
    </div>
    <div class="news-item">
      <div class="news-thumb" role="img" aria-label="Photo of a cloud network concept"></div>
      <div>
        <h5>Sed ut perspiciatis unde omnis</h5>
        <div class="news-date">18 - MARCH 2015</div>
        <p>We have opened new support hours for clients across the UK, with faster answers every working day.</p>
      </div>
    </div>
  </div>
  <div class="testimonials">
    <div class="col-title">TESTIMONIALS</div>
    <div class="quote">SkyVarro moved our whole office to the cloud over one weekend. Monday morning everything simply worked, and our monthly IT bill is lower than before. The team explains each step clearly and always answers quickly when we need help with something new.</div>
    <div class="quote-nav"><svg width="44" height="18" viewBox="0 0 44 18"><rect width="18" height="18" fill="#e3e7ea"/><path d="M11 4 6 9l5 5" fill="none" stroke="#7b848c" stroke-width="2"/><rect x="24" width="18" height="18" fill="#2a8bd0"/><path d="M31 4l5 5-5 5" fill="none" stroke="#fff" stroke-width="2"/></svg></div>
    <div class="person">
      <div class="avatar" role="img" aria-label="Client portrait"></div>
      <div><b>Marek Holt</b> <span>- IT Manager</span></div>
    </div>
  </div>
</section>

<footer class="footer">
  <div>
    <h6>COMPANY</h6>
    <p>SkyVarro limited is a UK cloud partner helping small and medium firms move safely from on premise systems to flexible, cost saving cloud services with friendly ongoing support.</p>
  </div>
  <div>
    <h6>QUICK LINKS</h6>
    <ul><li>Home</li><li>Features</li><li>Search Market</li><li>Legal Register</li><li>Contact</li></ul>
  </div>
  <div>
    <h6>OUR NEWSLETTER</h6>
    <p>Sign up for cloud tips, savings news and service updates sent to you once a month.</p>
    <div class="subscribe"><span>Email here</span><b>REGISTER</b></div>
  </div>
  <div>
    <h6>CONTACT US</h6>
    <p>SkyVarro limited<br>14 Harrowgate Lane, Leeds LS1 4QX</p>
    <p class="contact-line"><svg width="10" height="10" viewBox="0 0 10 10"><path d="M2 1h2l1 2-1 1q1 2 2 2l1-1 2 1v2q-5 0-7-7z" fill="#2fa5e6"/></svg>+44 (0) 1632 960 418</p>
    <p class="contact-line"><svg width="10" height="10" viewBox="0 0 10 10"><rect x="0.5" y="2" width="9" height="6" fill="none" stroke="#2fa5e6"/><path d="M1 2.5l4 3 4-3" fill="none" stroke="#2fa5e6"/></svg>hello@skyvarro-example.co.uk</p>
  </div>
</footer>
<div class="bottom">Copyright 2015 • SkyVarro limited • Terms • Privacy</div>
</body>
</html>
```